Establishing a website for a non profit organisation

The foundation is called:

German: Edle Alte Bruderschaft des Hofes Lindenmark e.V.

Englisch (Translation): Noble old Brotherhood of Court Lindenmark e.V.

The foundation is a legal nonprofit organization with the purpose to help people in need. The foundation - a charitable organization - donates funds and supports solely and directly people living in Frankfurt and in Germany.

In some cases the foundation works together with other charitable organizations that support projects to help people in need.

The foundation also functions as trustee with powers of administration of property in trust with a legal obligation to administer it solely for the purposes specified. The purpose is not to generate/obtain wealth for shareholders but to respectfully execute the benevolent intentions of the founders/testators in the interest of the legatee.

The foundation was established in 1408.

The website should give a good and easy overview about the foundation work.
It should be easy to figure out how to participate and help the organisation.
Either you can participate with a one time donation, with a regular donation or with a testament.

For those with donation it is possible to hand over an contribution receipt for tax purposes.

The main color should be red: RGB R:229 - G:47 - B:34

```html
<!DOCTYPE html>
<html lang="en">
<head>
<meta charset="utf-8">
<title>Edle Alte Bruderschaft des Hofes Lindenmark e.V.</title>
<link href="https://fonts.googleapis.com/css2?family=Gelasio:wght@400&family=Roboto:wght@300;400;500&display=swap" rel="stylesheet">
<style>
:root{
  --red:#e52f22;
  --olive:#5b5d4c;
  --text:#6d6d66;
  --hero:#dcdccf;
  --page:#fafbfa;
  --footer:#e4e4e3;
  --line:#cfcfcf;
}
*{margin:0;padding:0;box-sizing:border-box}
html,body{width:1024px;height:1200px;overflow:hidden}
body{position:relative;background:var(--page);font-family:'Roboto',sans-serif;color:var(--text)}
.abs{position:absolute}

.site-header{left:0;top:0;width:1024px;height:77px;background:linear-gradient(#f6f6f4,#eeeeec);border-bottom:1px solid #bdbdb6}
.brand{left:136px;top:22px;display:flex;align-items:center;gap:9px}
.brand-mark{width:12px;height:12px;background:var(--red);flex:none}
.brand-name{font-family:'Roboto',sans-serif;font-weight:400;font-size:12px;line-height:16px;color:var(--olive);width:200px}
.nav-item{top:0;height:77px;width:78px;text-align:center;font-family:'Gelasio',serif;font-size:12.5px;color:#7b7c70}
.nav-item svg{display:block;margin:22px auto 4px;width:11px;height:11px;fill:#8a8b80}
.nav-item.active{background:var(--red);color:#fff}
.nav-item.active svg{fill:#fff}

.hero{left:0;top:77px;width:1024px;height:397px;background:var(--hero);overflow:hidden}
.hero-photo{left:0;top:0;width:520px;height:397px;background:linear-gradient(90deg,#2a2521 0%,#4a4038 35%,#b9b6aa 70%,rgba(220,220,207,0) 100%)}
.hero-title{left:456px;top:95px;font-family:'Gelasio',serif;font-weight:400;font-size:50px;line-height:58px;color:#5d5f4d;letter-spacing:-.5px}
.hero-sub{left:458px;top:227px;font-size:19.5px;font-weight:300;color:#5d5f4d}
.btn-red{background:var(--red);color:#fff;font-weight:500;text-align:center;border:1px solid #c92418}
.btn-white{background:#fff;color:#7b7c70;font-weight:500;text-align:center;border:1px solid #c9c9c2}

h2{position:absolute;font-family:'Gelasio',serif;font-weight:400;font-size:20.5px;color:var(--olive)}
.photo{background:linear-gradient(135deg,#7a5a46,#b48d6f 45%,#5c6f83)}
.copy{font-size:10.3px;line-height:14.4px;font-weight:300;color:var(--text)}
.btn-more{width:64px;height:28px;font-size:9.5px;line-height:26px;text-align:center;color:#8a8a84;background:linear-gradient(#fcfcfc,#ececec);border:1px solid #c4c4c0;border-radius:2px}
.donations{list-style:none;font-size:10.3px;font-weight:300;line-height:19.2px}
.news-title{font-size:14.4px;font-weight:500;color:#55564a}
.read-more{font-size:10px;color:var(--red);text-decoration:underline}
.map{background:linear-gradient(135deg,#e8e4da,#d8d3c6 50%,#efe6cc)}
.contact-row{font-size:10.3px;font-weight:300;color:#7b7c70;line-height:16px}
.contact-row svg{position:absolute;left:-18px;top:1px;width:12px;height:12px;fill:#8a8b80}

.site-footer{left:0;top:1156px;width:1024px;height:44px;background:var(--footer);font-size:10.3px;color:#9a9a94;font-weight:300}
</style>
</head>
<body>

<header class="abs site-header">
  <div class="abs brand">
    <span class="brand-mark"></span>
    <span class="brand-name">Edle Alte Bruderschaft des Hofes Lindenmark e.V.</span>
  </div>
  <nav>
    <div class="abs nav-item active" style="left:382px"><svg viewBox="0 0 12 12"><path d="M6 1 0 6.5h1.7V11h3V8h2.6v3h3V6.5H12z"/></svg>Home</div>
    <div class="abs nav-item" style="left:467px"><svg viewBox="0 0 12 12"><path d="M2 1h7l1 1v9H3L2 10zM3 9v1h6V9z"/></svg>History</div>
    <div class="abs nav-item" style="left:560px"><svg viewBox="0 0 12 12"><circle cx="6" cy="6" r="5.5"/></svg>What We Do</div>
    <div class="abs nav-item" style="left:654px"><svg viewBox="0 0 12 12"><circle cx="6" cy="6" r="5.5"/><rect x="5.2" y="5" width="1.6" height="4.5" fill="#fff"/><circle cx="6" cy="3.3" r=".9" fill="#fff"/></svg>News</div>
    <div class="abs nav-item" style="left:732px"><svg viewBox="0 0 12 12"><path d="M2.5 1 5 3.5 3.8 5a7 7 0 0 0 3.2 3.2L8.5 7 11 9.5 9.5 11C5 11 1 7 1 2.5z"/></svg>Contact</div>
    <div class="abs nav-item" style="left:811px"><svg viewBox="0 0 12 12"><path d="M1 4h10v2.5H1zM2 7h8v4.5H2z"/><rect x="5.3" y="4" width="1.4" height="7.5" fill="#eee"/></svg>Donate</div>
  </nav>
</header>

<section class="abs hero">
  <div class="abs hero-photo" role="img" aria-label="Black and white portrait photograph of a young child looking into the camera"></div>
  <h1 class="abs hero-title">Give a little, make a<br>big difference.</h1>
  <p class="abs hero-sub">Changing lives. Changing the future.</p>
  <a class="abs btn-red" style="left:458px;top:278px;width:112px;height:36px;line-height:34px;font-size:13px">Donate Now</a>
  <a class="abs btn-white" style="left:578px;top:278px;width:112px;height:36px;line-height:34px;font-size:13px">Take Action</a>
</section>

<h2 style="left:136px;top:504px">History of Foundation</h2>
<div class="abs photo" style="left:135px;top:537px;width:240px;height:100px" role="img" aria-label="Photograph of a smiling group of young volunteers"></div>
<p class="abs copy" style="left:135px;top:651px;width:240px">It is a long established fact that a reader will be distracted by the readable content of a page when looking at its layout. The point of using Lorem Ipsum is that it has a more-or-less normal distribution of letters, as opposed to using 'Content here, content here', making it look like readable English.</p>
<a class="abs btn-more" style="left:134px;top:748px">Read More</a>

<h2 style="left:392px;top:504px">What We Do Today</h2>
<div class="abs photo" style="left:392px;top:536px;width:240px;height:101px;background:linear-gradient(135deg,#6b5446,#4d7fc1 45%,#7b8a6a)" role="img" aria-label="Photograph of a volunteer holding a baby surrounded by children"></div>
<p class="abs copy" style="left:392px;top:651px;width:240px">It is a long established fact that a reader will be distracted by the readable content of a page when looking at its layout. The point of using Lorem Ipsum is that it has a more-or-less normal distribution of letters, as opposed to using 'Content here, content here', making it look like readable English.</p>
<a class="abs btn-more" style="left:391px;top:748px">Read More</a>

<h2 style="left:647px;top:504px">Donate Now</h2>
<a class="abs btn-red" style="left:647px;top:540px;width:117px;height:36px;line-height:34px;font-size:12.5px">1-time Options</a>
<a class="abs btn-red" style="left:771px;top:540px;width:117px;height:36px;line-height:34px;font-size:12.5px">Lifetime Donation</a>
<p class="abs copy" style="left:647px;top:591px;width:240px">It is a long established fact that a reader will be distracted by the readable content of a page when looking at its layout.</p>

<h2 style="left:647px;top:664px">Received Donations</h2>
<ul class="abs donations" style="left:646px;top:699px">
  <li>- $300 from Harbor Lane Trading, Inc. (8/14/2013)</li>
  <li>- $300 from Harbor Lane Trading, Inc. (8/14/2013)</li>
  <li>- $300 from Harbor Lane Trading, Inc. (8/14/2013)</li>
  <li>- $300 from Harbor Lane Trading, Inc. (8/14/2013)</li>
</ul>

<h2 style="left:136px;top:814px">Recent News</h2>
<div class="abs photo" style="left:135px;top:858px;width:113px;height:100px;background:linear-gradient(135deg,#4a3a33,#8c6a5a 50%,#c9c3c8)" role="img" aria-label="Photograph of children holding a thank-you sign"></div>
<div class="abs news-title" style="left:266px;top:856px">Sample Headline/Title</div>
<p class="abs copy" style="left:266px;top:888px;width:360px">A page when looking at its layout. The point of using Lorem Ipsum is that it has a more-or-less normal distribution of letters, as opposed to using 'Content here, content here', making it look like readable English.</p>
<a class="abs read-more" style="left:266px;top:947px">READ MORE</a>

<div class="abs photo" style="left:135px;top:980px;width:113px;height:100px;background:linear-gradient(135deg,#b58a6a,#e2c3a8 50%,#c9a38a)" role="img" aria-label="Photograph of a smiling woman with a child"></div>
<div class="abs news-title" style="left:266px;top:978px">Sample Headline/Title</div>
<p class="abs copy" style="left:266px;top:1010px;width:360px">A page when looking at its layout. The point of using Lorem Ipsum is that it has a more-or-less normal distribution of letters, as opposed to using 'Content here, content here', making it look like readable English.</p>
<a class="abs read-more" style="left:266px;top:1069px">READ MORE</a>

<h2 style="left:649px;top:814px">Contact Us</h2>
<div class="abs map" style="left:649px;top:858px;width:237px;height:100px" role="img" aria-label="Street map showing the foundation's location"></div>
<div class="abs contact-row" style="left:676px;top:979px"><svg viewBox="0 0 12 12"><path d="M2.5 1 5 3.5 3.8 5a7 7 0 0 0 3.2 3.2L8.5 7 11 9.5 9.5 11C5 11 1 7 1 2.5z"/></svg>+1800-555-0142</div>
<div class="abs contact-row" style="left:676px;top:1003px"><svg viewBox="0 0 12 12"><path d="M1 2.5h10v7H1zm1 1v.3l4 2.8 4-2.8v-.3zm0 1.5v3.5h8V5L6 7.8z" fill-rule="evenodd"/></svg>info@lindenmark-trust.org</div>
<div class="abs contact-row" style="left:676px;top:1027px"><svg viewBox="0 0 12 12"><path d="M6 0a4 4 0 0 1 4 4c0 3-4 8-4 8S2 7 2 4a4 4 0 0 1 4-4zm0 2.5A1.5 1.5 0 1 0 6 5.5 1.5 1.5 0 0 0 6 2.5z" fill-rule="evenodd"/></svg>Your Address, Your Country<br>Your Zip Code</div>

<footer class="abs site-footer">
  <span class="abs" style="left:138px;top:15px">Copyright © 2014 - Company Name. All Rights reserved</span>
  <span class="abs" style="left:750px;top:15px">Privacy Policy</span>
  <span class="abs" style="left:848px;top:15px">Sitemap</span>
</footer>

</body>
</html>
```